Nanny Agency Needs a Newspaper Ad

We need a newspaper ad for a new company based in New York City called "Sitters by Lira". We place top sitters and nannies with families in Manhattan, The Hamptons, Brooklyn, and New Jersey. We do live-in, live-out, short term, long term, and one time jobs. Our most popular service is our saturday night sitter, where we get clients reliable sitters for saturday nights at low prices. We would like to see designs that use bright colors, like hot pink and teal. The final ad should represent our company, and should look a lot like our logo.

We are planning to put it in 'The Hearth Weekly' Magazine, so we want it to say that we have sitters who have experience with Jewish families and working in a Kosher home.

It should say that we are a nanny agency based in Manhattan, The Hamptons, New Jersey, and Brooklyn that does full time, part time, and one time placements with great screened nannies and sitters.

sittersbylira.example

Target Market(s)

Parents

Requirements
Must have
• Logo and colors of our logo.

```html
<!DOCTYPE html>
<html lang="en">
<head>
<meta charset="utf-8">
<title>Sitters by Lira – Newspaper Ad</title>
<link href="https://fonts.googleapis.com/css2?family=Arimo:wght@400;700&family=Roboto+Condensed:wght@700&display=swap" rel="stylesheet">
<style>
  :root {
    --page: #e8e6e3;
    --paper: #ffffff;
    --hot-pink: #f0147e;
    --teal: #2bb9a4;
    --tagline-grey: #6a6a6a;
    --band-grey: #6b6b6b;
    --band-black: #000000;
    --ink: #111111;
    --photo-light: #d9d9d9;
    --photo-dark: #5a5a5a;
  }
  * { margin: 0; padding: 0; box-sizing: border-box; }
  html, body { width: 1200px; height: 960px; overflow: hidden; background: var(--page); }
  body { position: relative; font-family: "Arimo", Arial, sans-serif; }

  .ad {
    position: absolute; left: 10px; top: 84px;
    width: 1180px; height: 792px;
    background: var(--paper);
    box-shadow: 0 2px 10px rgba(0,0,0,.18);
  }
  .ad__photo {
    position: absolute; left: 0; top: 0; width: 502px; height: 100%;
    background: linear-gradient(160deg, var(--photo-light) 0%, #a8a8a8 45%, var(--photo-dark) 100%);
  }
  .ad__content { position: absolute; left: 508px; top: 0; right: 0; bottom: 0; }

  .brand {
    position: absolute; left: 34px; top: 98px;
    display: flex; align-items: center; gap: 16px;
  }
  .brand__mark { width: 22px; height: 22px; border-radius: 50%; background: var(--hot-pink); }
  .brand__name {
    font-family: "Arimo", Arial, sans-serif; font-weight: 700;
    font-size: 62px; letter-spacing: -1.5px; color: var(--hot-pink); line-height: 1;
  }

  .tagline {
    position: absolute; left: 34px; top: 216px; width: 600px;
    font-family: "Roboto Condensed", "Arial Narrow", sans-serif; font-weight: 700;
    font-size: 27px; line-height: 30px; color: var(--tagline-grey); text-transform: uppercase;
  }

  .band { position: absolute; left: 0; right: 0; padding-left: 34px; color: #fff; }
  .band--services { top: 293px; height: 187px; background: var(--band-grey); padding-top: 28px; }
  .band--popular { top: 582px; height: 119px; background: var(--band-black); padding-top: 18px; padding-left: 36px; }

  .section-title { font-weight: 700; font-size: 24px; line-height: 28px; }
  .bullets { list-style: none; display: flex; gap: 12px; margin-top: 8px; font-size: 20px; line-height: 24px; }
  .bullets li::before { content: "•"; margin-right: 5px; }
  .services__note { margin-top: 22px; font-size: 20px; line-height: 27px; }

  .regions { position: absolute; left: 34px; top: 502px; color: var(--ink); }
  .regions .bullets { gap: 17px; }

  .popular__text { margin-top: 6px; font-size: 20px; line-height: 23px; width: 470px; }

  .contact { position: absolute; left: 40px; top: 716px; color: var(--ink); font-weight: 700; }
  .contact__phone { font-size: 22px; letter-spacing: .8px; line-height: 28px; }
  .contact__web { font-size: 19px; line-height: 28px; }
</style>
</head>
<body>
  <article class="ad">
    <div class="ad__photo" role="img" aria-label="Black and white photo of a smiling mother carrying her young daughter on her shoulders"></div>

    <div class="ad__content">
      <div class="brand">
        <span class="brand__mark"></span>
        <span class="brand__name">Sitters by Lira</span>
      </div>

      <p class="tagline">We have sitters who have experience with Jewish families &amp; working in a kosher home.</p>

      <section class="band band--services">
        <h2 class="section-title">SERVICES</h2>
        <ul class="bullets">
          <li>Live-in &amp; Live-out</li>
          <li>Short Term &amp; Long Term</li>
          <li>One Time Jobs</li>
        </ul>
        <p class="services__note">Providing Full time, Part time &amp; One time placements<br>with great screened nannies &amp; sitters.</p>
      </section>

      <section class="regions">
        <h2 class="section-title">SERVING CLIENTS In</h2>
        <ul class="bullets">
          <li>Manhattan</li>
          <li>The Hamptons</li>
          <li>New Jersey</li>
          <li>Brooklyn</li>
        </ul>
      </section>

      <section class="band band--popular">
        <h2 class="section-title">OUR MOST POPULAR SERVICE</h2>
        <p class="popular__text">Saturday night sitter, where we get clients reliable sitters for Saturday nights at low prices.</p>
      </section>

      <div class="contact">
        <p class="contact__phone">Call Us Today: 555-014-0192</p>
        <p class="contact__web">www.sittersbylira.example</p>
      </div>
    </div>
  </article>
</body>
</html>
```